New Business Card Design

We would like to refresh our business cards and make them look better. We are an IT company specialising in Cloud Services, IT Managed Services, software and hardware. I have attached a PSD of our current design. Also attached our logo.
Updates

I have uploaded all new logos in EPS format.

Can you please edit all designs to include a job title for Marcus Tovey, eg. General Manager

Industry/Entity Type

Software

Colors
ffffff

Requirements
Must have
• Please use white background.
Should not have
• Black background

```html
<!DOCTYPE html>
<html lang="en">
<head>
<meta charset="utf-8">
<title>Meridian Systems – Business Cards</title>
<link rel="stylesheet" href="https://fonts.googleapis.com/css2?family=Open+Sans:wdth,wght@75..100,300..700&display=swap">
<style>
  :root {
    --backdrop: #e6e4e1;
    --card-white: #ffffff;
    --card-shade: #e9eaec;
    --brand-red: #c0392b;
    --swoosh-grey: #8a939c;
    --text-grey: #55585c;
    --text-dark: #2b2d30;
    --rule-grey: #9a9ea3;
  }
  * { margin: 0; padding: 0; box-sizing: border-box; }
  html, body {
    width: 1200px;
    height: 1024px;
    overflow: hidden;
    background: var(--backdrop);
    font-family: "Open Sans", Arial, sans-serif;
  }
  .sheet {
    position: relative;
    width: 1200px;
    height: 1024px;
  }
  .card {
    position: absolute;
    left: 200px;
    width: 800px;
    height: 457px;
    border-radius: 4px;
    overflow: hidden;
    box-shadow: 0 6px 18px rgba(0,0,0,0.18);
    background: var(--card-white);
  }
  .card--front { top: 40px; }
  .card--back { top: 527px; }
  .card svg { display: block; width: 800px; height: 457px; }
  .wordmark {
    font-family: "Open Sans", Arial, sans-serif;
    font-weight: 300;
    fill: var(--text-grey);
  }
  .web-address {
    font-weight: 600;
    fill: var(--card-white);
    letter-spacing: 4px;
  }
  .holder-name {
    font-weight: 700;
    font-stretch: 75%;
    fill: var(--text-dark);
  }
  .holder-title {
    font-weight: 400;
    fill: var(--brand-red);
    letter-spacing: 1px;
  }
  .contact-line {
    font-weight: 400;
    fill: var(--text-grey);
  }
</style>
</head>
<body>
<main class="sheet">

  <!-- Front of card -->
  <section class="card card--front" aria-label="Business card front">
    <svg viewBox="0 0 800 457" xmlns="http://www.w3.org/2000/svg">
      <defs>
        <radialGradient id="frontFace" cx="45%" cy="40%" r="75%">
          <stop offset="0" stop-color="var(--card-white)"/>
          <stop offset="1" stop-color="var(--card-shade)"/>
        </radialGradient>
      </defs>
      <rect class="card-face" width="800" height="457" fill="url(#frontFace)"/>
      <path class="swoosh-grey" d="M420,318 C610,270 735,160 780,0 L800,0 L800,8 C760,170 640,288 420,318 Z" fill="var(--swoosh-grey)"/>
      <path class="band-red" d="M0,457 C330,450 640,350 800,60 L800,457 Z" fill="var(--brand-red)"/>
      <circle class="brand-dot" cx="120" cy="200" r="30" fill="var(--brand-red)"/>
      <text class="wordmark" x="166" y="215" font-size="42" letter-spacing="2">meridian systems</text>
      <text class="web-address" x="470" y="432" font-size="19" transform="rotate(-22 470 432)">WWW.MERIDIANSYS.COM.AU</text>
    </svg>
  </section>

  <!-- Back of card -->
  <section class="card card--back" aria-label="Business card back">
    <svg viewBox="0 0 800 457" xmlns="http://www.w3.org/2000/svg">
      <defs>
        <radialGradient id="backFace" cx="50%" cy="35%" r="75%">
          <stop offset="0" stop-color="var(--card-white)"/>
          <stop offset="1" stop-color="var(--card-shade)"/>
        </radialGradient>
      </defs>
      <rect class="card-face" width="800" height="457" fill="url(#backFace)"/>
      <path class="swoosh-grey" d="M120,430 C380,420 620,360 800,205 L800,225 C630,385 380,440 120,430 Z" fill="var(--swoosh-grey)"/>
      <path class="band-red" d="M0,457 C300,455 620,410 800,270 L800,457 Z" fill="var(--brand-red)"/>

      <circle class="brand-dot" cx="110" cy="80" r="26" fill="var(--brand-red)"/>
      <text class="wordmark" x="152" y="94" font-size="38" letter-spacing="2">meridian systems</text>

      <text class="holder-name" x="720" y="170" font-size="40" text-anchor="end">Marcus Tovey</text>
      <text class="holder-title" x="720" y="198" font-size="17" text-anchor="end">General Manager</text>
      <line class="divider" x1="80" y1="218" x2="720" y2="218" stroke="var(--rule-grey)" stroke-width="1.2"/>

      <g class="contact-list" font-size="17">
        <g class="contact contact--phone">
          <circle cx="300" cy="249" r="11" fill="var(--brand-red)"/>
          <path d="M295,243 q-2,6 4,12 q4,3 6,1 l-2,-3 -2,1 q-3,-2 -4,-5 l1,-2 z" fill="var(--card-white)"/>
          <text class="contact-line" x="322" y="255">07 3555 0147</text>
        </g>
        <g class="contact contact--mobile">
          <circle cx="300" cy="277" r="11" fill="var(--brand-red)"/>
          <rect x="296" y="270" width="8" height="14" rx="1.5" fill="var(--card-white)"/>
          <text class="contact-line" x="322" y="283">0400 555 219</text>
        </g>
        <g class="contact contact--email">
          <circle cx="300" cy="305" r="11" fill="var(--brand-red)"/>
          <rect x="294" y="300" width="12" height="9" fill="var(--card-white)"/>
          <path d="M294,300 L300,305 L306,300" stroke="var(--brand-red)" stroke-width="1.2" fill="none"/>
          <text class="contact-line" x="322" y="311">mtovey@meridiansys.com.au</text>
        </g>
        <g class="contact contact--web">
          <circle cx="300" cy="333" r="11" fill="var(--brand-red)"/>
          <circle cx="300" cy="333" r="6" stroke="var(--card-white)" stroke-width="1.3" fill="none"/>
          <line x1="294" y1="333" x2="306" y2="333" stroke="var(--card-white)" stroke-width="1.2"/>
          <ellipse cx="300" cy="333" rx="2.5" ry="6" stroke="var(--card-white)" stroke-width="1.2" fill="none"/>
          <text class="contact-line" x="322" y="339">www.meridiansys.com.au</text>
        </g>
      </g>
    </svg>
  </section>

</main>
</body>
</html>
```